Design a Book Cover for Android Development Book

I need to create an eBook design for a technical book with the following info.
Title: Quickstep Mobile - Turn Into An App Builder Within Three Months!
Subtitle: Discover ways to Make 12 Finished Phone Programs using Zephyr.
Author: Tem Barrowby
Delivery should include all book cover formats, 2D, 3D, Kindle, Print, etc.
Target Market(s)
People who want to learn Android development, people who want to switch careers to programming.
Industry/Entity Type
Programming
Colors
fec214
0792cd
ec1f27
Requirements
Should not have
- Do not use Android logo (green robot), Do not use Kotlin logo (K).

```html
<!DOCTYPE html>
<html lang="en">
<head>
<meta charset="utf-8">
<title>Quickstep Mobile – Book Cover</title>
<link rel="stylesheet" href="https://fonts.googleapis.com/css2?family=Comfortaa:wght@700&family=Montserrat:wght@300;400;500;800&display=swap">
<style>
  :root {
    --backdrop: #5e5e5e;
    --cover-gold: #a97d00;
    --title-gold: #b88a00;
    --headline-gold: #c8a002;
    --paper: #ececea;
    --device: #000000;
    --device-edge: #2a2a2a;
    --body-grey: #5a5a5a;
    --ink: #111111;
  }
  * { margin: 0; padding: 0; box-sizing: border-box; }
  html, body {
    width: 1200px; height: 1200px; overflow: hidden;
    background: var(--backdrop);
  }
  .book-cover {
    position: absolute; left: 233px; top: 50px;
    width: 734px; height: 1100px;
    background: var(--paper);
    overflow: hidden;
  }
  .cover-top {
    position: absolute; left: 0; top: 0;
    width: 100%; height: 580px;
    background: var(--cover-gold);
  }
  .device {
    position: absolute; left: 157px; top: 156px;
    width: 422px; height: 424px;
    background: var(--device);
    border-radius: 20px 20px 0 0;
    overflow: hidden;
  }
  .device-screen {
    position: absolute; left: 19px; top: 20px; right: 19px; bottom: -20px;
    border: 1.5px solid var(--device-edge);
    border-radius: 10px 10px 0 0;
  }
  .device-camera {
    position: absolute; left: 50%; top: 41px;
    width: 14px; height: 14px; margin-left: -7px;
    background: var(--title-gold); border-radius: 50%;
  }
  .book-title {
    position: absolute; left: 38px; right: 24px; top: 248px;
    font-family: "Comfortaa", sans-serif; font-weight: 700;
    font-size: 70px; line-height: 74px; letter-spacing: -2px;
    color: var(--title-gold);
    white-space: nowrap;
  }
  .cover-text {
    position: absolute; left: 204px; top: 640px; right: 30px;
    font-family: "Montserrat", sans-serif;
  }
  .headline {
    font-size: 36px; line-height: 44px; font-weight: 500;
    color: var(--headline-gold); text-transform: uppercase;
    letter-spacing: 0.5px;
  }
  .headline strong { font-weight: 800; }
  .subtitle {
    margin-top: 30px;
    font-size: 17px; line-height: 35px; font-weight: 500;
    color: var(--body-grey); text-transform: uppercase; letter-spacing: 1px;
  }
  .author {
    position: absolute; left: 204px; top: 996px;
    font-family: "Montserrat", sans-serif;
    font-size: 48px; line-height: 1; color: var(--ink);
    text-transform: uppercase; letter-spacing: 1px;
    white-space: nowrap;
  }
  .author .first { font-weight: 800; }
  .author .last { font-weight: 300; }
</style>
</head>
<body>
  <main class="book-cover">
    <section class="cover-top">
      <div class="device">
        <div class="device-screen"></div>
        <div class="device-camera"></div>
        <h1 class="book-title">quickstep<br>mobile</h1>
      </div>
    </section>
    <section class="cover-text">
      <p class="headline">Turn into<br>an app<br>builder within<br><strong>three months!</strong></p>
      <p class="subtitle">Discover ways to<br>make 12 finished<br>phone programs<br>using Zephyr.</p>
    </section>
    <p class="author"><span class="first">Tem</span><span class="last">Barrowby</span></p>
  </main>
</body>
</html>
```